Scandinavian Style Label for Vitamin (B-Complex) Bottle, 500mg

The Brand name is: Sun to Sun- Slogan Rise Brighter!
The bottle will be brown see-through plastic, cap also plastic(same color).
Label color should be in lighter shades, also would like to add the color gold. Brand name will be in gold as well.
Want it to be tasty and eye-catching. Could use contrasting colors that are visible from far.
Should have Supports Energy Metabolism, and Supports Heart Health written on them. Also needs Lactose and Gluten Free, Good Manufacturing signs.
Will include 60 coated caplets.
Label width is 180mm and height 70mm.
Label nutritional facts attached as a file.
Will be in English

Target Market(s)

Scandinavia, Russia

Industry/Entity Type

Vitamin

Font styles to use
Serif
Sans Serif
Script

Colors

Designer to choose colors to be used in the design.

Requirements
Must have
• Tasty touch of gold, elegance
Nice to have
• Vectors, dots, lines, drops
Should not have
• No dark colors and not too many colors

```html
<!DOCTYPE html>
<html lang="en">
<head>
<meta charset="utf-8">
<title>Sun to Sun Vitamins – B-Complex Label</title>
<link href="https://fonts.googleapis.com/css2?family=Oswald:wght@600&family=Playfair+Display:ital@1&family=Montserrat:wght@400;600&family=Roboto+Condensed:wght@700&display=swap" rel="stylesheet">
<style>
  :root {
    --page: #ffffff;
    --label-light: #fbf4ee;
    --label-rose: #efd9cb;
    --bronze: #a3705d;
    --bronze-dark: #7a5140;
    --gold: #d9a62c;
    --gold-light: #f6d77a;
    --gold-deep: #b9861c;
    --silver: #e6e6e6;
    --silver-dark: #a5a5a5;
    --ink: #4a3127;
    --white: #ffffff;
  }
  * { box-sizing: border-box; margin: 0; padding: 0; }
  html, body { width: 1200px; height: 899px; overflow: hidden; background: var(--page); }
  .canvas { position: relative; width: 1200px; height: 899px; }

  .label {
    position: absolute; left: 60px; width: 1080px; height: 420px;
    background: linear-gradient(90deg, var(--label-rose) 0%, var(--label-light) 30%, var(--white) 50%, var(--label-light) 70%, var(--label-rose) 100%);
    border: 1px solid var(--label-rose);
  }
  .label--classic { top: 20px; }
  .label--bold { top: 459px; }

  .label__rule { position: absolute; top: 30px; bottom: 30px; width: 2px;
    background: linear-gradient(180deg, transparent, var(--gold), transparent); }
  .label__rule--left { left: 240px; }
  .label__rule--right { right: 240px; }
  .label__band { position: absolute; left: 0; right: 0; height: 6px; background: linear-gradient(90deg, var(--gold-deep), var(--gold-light), var(--gold-deep)); }
  .label__band--top { top: 0; }
  .label__band--bottom { bottom: 0; }

  .front { position: absolute; left: 242px; width: 596px; top: 6px; bottom: 6px;
    display: flex; flex-direction: column; align-items: center; padding-top: 20px; }

  .brand-mark { display: flex; align-items: center; gap: 10px; color: var(--gold-deep); font-family: "Montserrat", sans-serif; font-weight: 400; }
  .brand-mark__dot { border-radius: 50%; background: var(--gold); }
  .label--classic .brand-mark { font-size: 26px; }
  .label--classic .brand-mark__dot { width: 44px; height: 44px; }
  .label--bold .brand-mark { font-size: 11px; gap: 6px; }
  .label--bold .brand-mark__dot { width: 18px; height: 18px; }

  .brand-name { font-family: "Oswald", sans-serif; font-weight: 600; font-size: 50px; line-height: 1.05; color: var(--gold-deep); letter-spacing: 1px; margin-top: 2px; }

  .slogan { font-family: "Playfair Display", serif; font-style: italic; font-size: 22px; line-height: 1.3; color: var(--ink); margin-top: 4px; }

  .benefits { display: flex; gap: 14px; margin-top: 6px; font-family: "Roboto Condensed", sans-serif; font-weight: 700; font-size: 15px; color: var(--ink); }
  .benefit { display: flex; align-items: center; gap: 5px; }

  .main-row { display: flex; align-items: center; gap: 34px; margin-top: 14px; }
  .visuals { display: flex; align-items: center; gap: 14px; }
  .visual-heart { width: 90px; height: 108px; border-radius: 45px 45px 50% 50%; background: radial-gradient(circle at 50% 60%, var(--gold-light), var(--gold-deep)); }
  .visual-dna { width: 84px; height: 84px; border-radius: 50%; background: radial-gradient(circle, #5a3a2e, #3a241c); border: 2px solid var(--gold); }

  .product { display: flex; flex-direction: column; align-items: center; }
  .product__title { font-family: "Montserrat", sans-serif; font-weight: 600; font-size: 30px; line-height: 1.1; letter-spacing: 5px; color: var(--bronze-dark); }

  .strength { display: flex; height: 32px; margin-top: 4px; border-radius: 16px; overflow: hidden; font-family: "Roboto Condensed", sans-serif; font-weight: 700; font-size: 20px; line-height: 32px; box-shadow: 0 1px 2px rgba(74,49,39,.3); }
  .strength__name { background: linear-gradient(180deg, var(--white), var(--silver) 50%, var(--silver-dark)); color: var(--ink); padding: 0 6px 0 14px; }
  .strength__dose { background: linear-gradient(180deg, var(--gold-light), var(--gold-deep)); color: var(--ink); padding: 0 14px 0 6px; }

  .count { position: relative; margin-top: 8px; width: 180px; height: 48px; }
  .count svg { position: absolute; inset: 0; }
  .count__text { position: absolute; inset: 0; padding-top: 6px; display: flex; align-items: center; justify-content: center; gap: 3px; font-family: "Roboto Condensed", sans-serif; font-weight: 700; color: var(--ink); }
  .count__words { font-size: 13px; line-height: 1; }
  .count__number { font-family: "Montserrat", sans-serif; font-size: 30px; font-weight: 400; line-height: 1; }

  .certs { display: flex; gap: 8px; margin-top: 8px; }
  .cert { width: 28px; height: 28px; border-radius: 50%; background: var(--gold); display: flex; align-items: center; justify-content: center; }
</style>
</head>
<body>
<main class="canvas">

  <section class="label label--classic">
    <span class="label__band label__band--top"></span>
    <span class="label__band label__band--bottom"></span>
    <span class="label__rule label__rule--left"></span>
    <span class="label__rule label__rule--right"></span>
    <div class="front">
      <div class="brand-mark"><span class="brand-mark__dot"></span>Sun to Sun Vitamins</div>
      <p class="slogan">Rise Brighter!</p>
      <div class="benefits">
        <span class="benefit"><svg width="16" height="16" viewBox="0 0 16 16"><circle cx="8" cy="8" r="7" fill="none" stroke="#d9a62c" stroke-width="1.5"/><path d="M9 3 5 9h3l-1 4 4-6H8z" fill="#d9a62c"/></svg>Energy Metabolism</span>
        <span class="benefit"><svg width="16" height="16" viewBox="0 0 16 16"><circle cx="8" cy="8" r="7" fill="none" stroke="#d9a62c" stroke-width="1.5"/><path d="M3 8h3l1-3 2 6 1-3h3" fill="none" stroke="#d9a62c" stroke-width="1.3"/></svg>Heart Health</span>
      </div>
      <div class="main-row">
        <div class="visuals">
          <div class="visual-heart" role="img" aria-label="Golden heart with growing tree and roots"></div>
          <div class="visual-dna" role="img" aria-label="DNA helix in a dark circle"></div>
        </div>
        <div class="product">
          <h1 class="product__title">VITAMIN</h1>
          <div class="strength"><span class="strength__name">B-COMPLEX</span><span class="strength__dose">500MG</span></div>
          <div class="count">
            <svg width="180" height="48" viewBox="0 0 180 48"><path d="M0 46 C28 46 28 4 56 4 H124 C152 4 152 46 180 46 Z" fill="#d9a62c"/></svg>
            <div class="count__text"><span class="count__words">COATED<br>CAPLETS</span><span class="count__number">60</span></div>
          </div>
          <div class="certs">
            <span class="cert"><svg width="14" height="14" viewBox="0 0 14 14"><path d="M2 7l3 3 7-7" fill="none" stroke="#fff" stroke-width="2"/></svg></span>
            <span class="cert"><svg width="14" height="14" viewBox="0 0 14 14"><path d="M2 7l3 3 7-7" fill="none" stroke="#fff" stroke-width="2"/></svg></span>
            <span class="cert"><svg width="14" height="14" viewBox="0 0 14 14"><path d="M2 7l3 3 7-7" fill="none" stroke="#fff" stroke-width="2"/></svg></span>
            <span class="cert"><svg width="14" height="14" viewBox="0 0 14 14"><path d="M2 7l3 3 7-7" fill="none" stroke="#fff" stroke-width="2"/></svg></span>
          </div>
        </div>
      </div>
    </div>
  </section>

  <section class="label label--bold">
    <span class="label__band label__band--top"></span>
    <span class="label__band label__band--bottom"></span>
    <span class="label__rule label__rule--left"></span>
    <span class="label__rule label__rule--right"></span>
    <div class="front">
      <div class="brand-mark"><span class="brand-mark__dot"></span>Sun to Sun Vitamins</div>
      <p class="brand-name">SUN TO SUN</p>
      <p class="slogan">Rise Brighter!</p>
      <div class="benefits">
        <span class="benefit"><svg width="16" height="16" viewBox="0 0 16 16"><circle cx="8" cy="8" r="7" fill="none" stroke="#d9a62c" stroke-width="1.5"/><path d="M9 3 5 9h3l-1 4 4-6H8z" fill="#d9a62c"/></svg>Energy Metabolism</span>
        <span class="benefit"><svg width="16" height="16" viewBox="0 0 16 16"><circle cx="8" cy="8" r="7" fill="none" stroke="#d9a62c" stroke-width="1.5"/><path d="M3 8h3l1-3 2 6 1-3h3" fill="none" stroke="#d9a62c" stroke-width="1.3"/></svg>Heart Health</span>
      </div>
      <div class="main-row">
        <div class="visuals">
          <div class="visual-heart" role="img" aria-label="Golden heart with growing tree and roots"></div>
          <div class="visual-dna" role="img" aria-label="DNA helix in a dark circle"></div>
        </div>
        <div class="product">
          <h1 class="product__title">VITAMIN</h1>
          <div class="strength"><span class="strength__name">B-COMPLEX</span><span class="strength__dose">500MG</span></div>
          <div class="count">
            <svg width="180" height="48" viewBox="0 0 180 48"><path d="M0 46 C28 46 28 4 56 4 H124 C152 4 152 46 180 46 Z" fill="#d9a62c"/></svg>
            <div class="count__text"><span class="count__words">COATED<br>CAPLETS</span><span class="count__number">60</span></div>
          </div>
          <div class="certs">
            <span class="cert"><svg width="14" height="14" viewBox="0 0 14 14"><path d="M2 7l3 3 7-7" fill="none" stroke="#fff" stroke-width="2"/></svg></span>
            <span class="cert"><svg width="14" height="14" viewBox="0 0 14 14"><path d="M2 7l3 3 7-7" fill="none" stroke="#fff" stroke-width="2"/></svg></span>
            <span class="cert"><svg width="14" height="14" viewBox="0 0 14 14"><path d="M2 7l3 3 7-7" fill="none" stroke="#fff" stroke-width="2"/></svg></span>
            <span class="cert"><svg width="14" height="14" viewBox="0 0 14 14"><path d="M2 7l3 3 7-7" fill="none" stroke="#fff" stroke-width="2"/></svg></span>
          </div>
        </div>
      </div>
    </div>
  </section>

</main>
</body>
</html>
```